Business Card for Makeup Artist

I need a business card designed for my makeup and hair artistry business which is primarily events and weddings focused. The card needs to be sleek, simple, stylish and appealing to women. I would prefer a white background but open to suggestions also. I also love the marble background look. I have attached some example pics. It needs to be a double sided card with logo and/or design on one side and contact details in the centre of the card on the other side. NO LOGO ON BACK. Examples attached.

Target Market(s)

Females age 14-55

Industry/Entity Type

Business

Contact Information for Business Card

Nora Vint
Principal Makeup Artist
P: 0413 925 214
E: nora@lumirabeauty.com.au
W: www.lumirabeauty.com.au

Requirements
Should not have
• No yellow, green, red or blue in the design.

```html
<!DOCTYPE html>
<html lang="en">
<head>
<meta charset="UTF-8">
<title>Lumira Beauty – Business Card</title>
<link href="https://fonts.googleapis.com/css2?family=Open+Sans:wght@300;400;600;700&display=swap" rel="stylesheet">
<style>
  :root {
    --page: #ecebea;
    --card-dark: #616161;
    --card-light: #ffffff;
    --ink-soft: #4a4a4a;
    --accent: #e94fc6;
    --white: #ffffff;
  }
  * { box-sizing: border-box; margin: 0; padding: 0; }
  html, body {
    width: 1200px;
    height: 900px;
    overflow: hidden;
    background: var(--page);
    font-family: "Open Sans", Arial, sans-serif;
  }
  .sheet {
    width: 1200px;
    height: 900px;
    display: flex;
    align-items: center;
    justify-content: center;
    gap: 60px;
  }
  .card {
    position: relative;
    width: 525px;
    height: 300px;
    box-shadow: 0 10px 28px rgba(0,0,0,0.18);
  }
  .card--front { background: var(--card-dark); }
  .card--back {
    background: var(--card-light);
    display: flex;
    align-items: center;
    justify-content: center;
  }

  .brand {
    position: absolute;
    left: 50%;
    top: 50%;
    transform: translate(-50%, -50%);
    display: flex;
    flex-direction: column;
    align-items: flex-start;
    color: var(--white);
  }
  .brand__name {
    font-weight: 600;
    font-size: 50px;
    line-height: 1;
    letter-spacing: 0.5px;
  }
  .brand__tagline {
    font-weight: 300;
    font-size: 17px;
    letter-spacing: 1px;
    margin-top: 4px;
    margin-left: 48px;
  }

  .contact {
    color: var(--ink-soft);
    text-align: left;
  }
  .contact__name {
    color: var(--accent);
    font-weight: 600;
    font-size: 17px;
    line-height: 1.2;
  }
  .contact__role {
    font-size: 12.5px;
    margin-top: 2px;
    margin-left: 12px;
  }
  .contact__list {
    list-style: none;
    margin-top: 22px;
    margin-left: 24px;
    font-size: 12.5px;
    line-height: 1.8;
  }
  .contact__label {
    color: var(--accent);
    font-weight: 700;
    margin-right: 4px;
  }
</style>
</head>
<body>
  <main class="sheet">
    <section class="card card--front" aria-label="Card front">
      <div class="brand">
        <span class="brand__name">Lumira</span>
        <span class="brand__tagline">MAKEUP ARTISTRY</span>
      </div>
    </section>

    <section class="card card--back" aria-label="Card back">
      <div class="contact">
        <p class="contact__name">Nora Vint</p>
        <p class="contact__role">Principal Makeup Artist</p>
        <ul class="contact__list">
          <li><span class="contact__label">T:</span>0413 925 214</li>
          <li><span class="contact__label">E:</span>nora@lumirabeauty.com.au</li>
          <li><span class="contact__label">W:</span>www.lumirabeauty.com.au</li>
        </ul>
      </div>
    </section>
  </main>
</body>
</html>
```